Personal Brand (Influencer) Website

I'm looking for a brand new website design for a youtuber/influencer Dane Whitaker.

I'm looking for a sleek design that is visually appealing while still maintaining full functionality and user experience.

Here is our current website: http://danewhitakerhq.example/

I want to combine some of the best elements and designs from the following websites.

https://www.milofenwright.example/
https://www.renzovale.example/
https://quinnbarlow.example/
https://www.silasmerrow.example/
http://danewhitakerhq.example/
http://www.kenfrayle.example/

Here are the different tabs that I would need designed as well as the main page:

Home Page (main page)
Blogs
My story (about me)
Top 100 book list
Contact

Here are several links and social media handles for you to get a better gauge on the branding of Dane Whitaker:
https://www.videohub.example/channel/XQpar3k9v-T2mhZZ_QWrta7z
https://trend-rocket.example/market-blog/uncategorized/dane-whitaker-entrepreneur-winning-market-follow-data-ep-17/
https://danelisten2.pagepath.example/optin-48203917
https://www.snapgrid.example/officialdanewhitaker/

```html
<!DOCTYPE html>
<html lang="en">
<head>
<meta charset="utf-8">
<title>Dane Whitaker — Live Life On Your Terms</title>
<link rel="stylesheet" href="https://fonts.googleapis.com/css2?family=Lato:ital,wght@0,400;0,700;1,400&family=Trocchi&display=swap">
<style>
:root{
  --blue:#1e8fe0;
  --blue-deep:#1479c9;
  --ink:#222;
  --muted:#888;
  --field:#f2f2f2;
  --light:#f1f1f1;
  --footer:#333;
  --white:#fff;
}
*{box-sizing:border-box;margin:0;padding:0}
html,body{width:1200px;height:2848px;overflow:hidden}
body{position:relative;font-family:'Lato',sans-serif;color:var(--ink);background:var(--white)}
.abs{position:absolute}
.serif{font-family:'Trocchi',serif}

/* hero */
.hero{left:0;top:0;width:1200px;height:648px;background:linear-gradient(160deg,#4a5a4e 0%,#7a7060 35%,#a79d8d 60%,#5d5a52 100%)}
.hero-photo{left:0;top:0;width:1200px;height:648px;background:radial-gradient(ellipse at 30% 55%,rgba(200,190,170,.35),transparent 60%),radial-gradient(ellipse at 75% 80%,rgba(240,240,240,.3),transparent 55%)}
.brand{left:78px;top:30px;height:36px;display:flex;align-items:center;gap:10px;color:var(--white);font-weight:700;font-size:27px;letter-spacing:2px}
.brand-mark{width:22px;height:22px;background:var(--white)}
.nav{right:78px;top:36px;display:flex;gap:26px;font-size:17px;color:var(--white)}
.nav-rule{left:78px;top:93px;width:1046px;height:1px;background:rgba(255,255,255,.45)}
.hero-name{left:78px;top:292px;font-size:47px;color:var(--white);letter-spacing:.5px}
.hero-tag{left:78px;top:372px;font-size:29px;color:var(--white)}
.social-card{left:596px;top:262px;width:604px;height:193px}
.avatar-label{left:628px;top:405px;font-size:19px;color:#6ec0f0;letter-spacing:.5px}
.social-list{left:908px;top:278px;width:216px}
.social-row{display:flex;align-items:center;gap:20px;height:53px;border-bottom:1px solid rgba(255,255,255,.18);color:var(--white);font-size:14px}
.social-dot{width:18px;height:18px;border-radius:50%;border:2px solid #ccc}

/* signup */
.signup-title{left:0;top:696px;width:1200px;text-align:center;font-size:34px}
.signup-sub{left:0;top:754px;width:1200px;text-align:center;font-size:17px;color:var(--muted)}
.field{top:804px;height:46px;background:var(--field);color:#666;font-size:15px;padding:14px 24px}
.btn{background:var(--blue);color:var(--white);font-weight:700;font-size:20px;text-align:center;border-radius:3px}

/* meet */
.meet{left:0;top:930px;width:1200px;height:500px;background:linear-gradient(180deg,var(--blue) 0%,#2a9af0 100%)}
.video{left:78px;top:1015px;width:488px;height:333px;background:linear-gradient(135deg,#2a2540 0%,#3a3535 50%,#1e1e22 100%)}
.meet-title{left:652px;top:1052px;font-size:40px;color:var(--white)}
.meet-copy{left:652px;top:1112px;width:470px;font-size:15.5px;line-height:25px;color:var(--white)}
.meet-copy p+p{margin-top:10px}
.btn-white{left:656px;top:1266px;width:187px;height:46px;background:var(--white);color:var(--blue);font-weight:700;font-size:20px;line-height:46px;text-align:center;border-radius:3px}

/* course */
.course-art{left:158px;top:1512px;width:885px;height:418px;background:linear-gradient(180deg,#8a86b0 0%,#c9c4d6 35%,#6f6888 65%,#3c3658 100%);box-shadow:0 8px 24px rgba(0,0,0,.25)}
.course-frame{left:174px;top:1528px;width:853px;height:386px;border:6px solid rgba(255,255,255,.55)}
.course-rule{left:540px;top:1614px;width:120px;height:3px;background:var(--white)}
.course-art-text{left:158px;top:1650px;width:885px;text-align:center;font-size:26px;line-height:38px;color:#1f1f2a}
.course-title{left:0;top:1980px;width:1200px;text-align:center;font-size:34px}
.course-lead{left:0;top:2044px;width:1200px;text-align:center;font-size:18px;font-style:italic;color:#444}
.course-copy{left:230px;top:2080px;width:740px;text-align:center;font-size:15px;line-height:25px;color:#555}

/* posts */
.posts{left:0;top:2285px;width:1200px;height:420px;background:var(--light)}
.posts-title{left:0;top:2336px;width:1200px;text-align:center;font-size:38px}
.thumb{top:2400px;width:322px;height:208px;box-shadow:0 4px 12px rgba(0,0,0,.25)}
.thumb-title{position:absolute;left:16px;top:14px;color:var(--white);font-size:17px;font-weight:700;white-space:nowrap}

/* footer */
.footer{left:0;top:2705px;width:1200px;height:143px;background:var(--footer)}
.footer-nav{left:0;top:2741px;width:1200px;text-align:center;color:var(--white);font-size:16px;word-spacing:4px}
.footer-copy{left:0;top:2790px;width:1200px;text-align:center;color:var(--white);font-size:15px}
</style>
</head>
<body>

<header>
  <div class="abs hero" role="img" aria-label="Blurred photo of a man in a hat sitting on rocks beside a mountain waterfall"></div>
  <div class="abs hero-photo"></div>
  <div class="abs brand"><span class="brand-mark"></span>DANE WHITAKER</div>
  <nav class="abs nav"><span>HOME</span><span>BLOG</span><span>MT STORY</span><span>TOP 100 BOOKS</span><span>CONTACT</span></nav>
  <div class="abs nav-rule"></div>
  <h1 class="abs hero-name serif">DANE WHITAKER</h1>
  <p class="abs hero-tag">Live Life On Your Terms</p>

  <svg class="abs social-card" viewBox="0 0 604 193" aria-hidden="true">
    <path d="M130 0 H604 V193 H28 A130 130 0 0 1 130 0 Z" fill="rgba(35,40,50,.8)"/>
    <path d="M28 193 A130 130 0 0 1 150 6" fill="none" stroke="#fff" stroke-width="9"/>
    <circle cx="124" cy="68" r="62" fill="#1f2630" stroke="#1e8fe0" stroke-width="4"/>
    <circle cx="124" cy="68" r="56" fill="#5a6470"/>
    <circle cx="262" cy="22" r="18" fill="rgba(255,255,255,.05)"/>
    <circle cx="420" cy="170" r="40" fill="rgba(255,255,255,.05)"/>
  </svg>
  <div class="abs" style="left:664px;top:274px;width:112px;height:112px;border-radius:50%" role="img" aria-label="Portrait photo of Dane Whitaker"></div>
  <p class="abs avatar-label">DANE WHITAKER</p>
  <ul class="abs social-list" style="list-style:none">
    <li class="social-row"><span class="social-dot"></span>Dane Whitaker</li>
    <li class="social-row"><span class="social-dot"></span>officialdanewhitaker</li>
    <li class="social-row"><span class="social-dot"></span>Dane Whitaker</li>
  </ul>
</header>

<section>
  <h2 class="abs signup-title serif">Join 40,000+ Zonara Sellers.</h2>
  <p class="abs signup-sub">Sign up for the latest videos &amp; free content.</p>
  <div class="abs field" style="left:142px;width:354px">Your Name</div>
  <div class="abs field" style="left:506px;width:354px">Your Email</div>
  <div class="abs btn" style="left:872px;top:804px;width:186px;height:46px;line-height:46px">GET STARTED</div>
</section>

<section>
  <div class="abs meet" role="img" aria-label="Blue-tinted mountain range backdrop"></div>
  <div class="abs video" role="img" aria-label="Video still of Dane Whitaker in a studio"></div>
  <svg class="abs" style="left:277px;top:1136px" width="90" height="90" viewBox="0 0 90 90" aria-hidden="true">
    <circle cx="45" cy="45" r="40" fill="none" stroke="#1e8fe0" stroke-width="4"/>
    <path d="M35 26 L64 45 L35 64 Z" fill="none" stroke="#1e8fe0" stroke-width="4" stroke-linejoin="round"/>
  </svg>
  <h2 class="abs meet-title serif">Meet Dane Whitaker</h2>
  <div class="abs meet-copy">
    <p>Dane Whitaker is a 7 figure Ecommerce Entrepreneur, Speaker, Inventor, Bio-hacker, and Positive thinker. He believes the world is getting better every day.</p>
    <p>Dane went from 0 to 6 Million in 6 Months selling Eclipse Glasses on Zonara Fulfilled. He also proposed to his wife in Outer Space.</p>
  </div>
  <div class="abs btn-white">KNOW MORE</div>
</section>

<section>
  <div class="abs course-art" role="img" aria-label="Snowy mountain valley landscape"></div>
  <div class="abs course-frame"></div>
  <div class="abs course-rule"></div>
  <p class="abs course-art-text">Live Life On Your Terms With My<br>Free Zonara Private Label Course</p>
  <h2 class="abs course-title serif">The First Free Zonara Private Label Course</h2>
  <p class="abs course-lead">I am giving away everything that I know for free.</p>
  <p class="abs course-copy">Myself &amp; the top Zonara sellers will be teaching you everything that you need to know about creating &amp; managing a thriving Zonara Fulfilled Business so that you can live your life on your terms.</p>
  <div class="abs btn" style="left:507px;top:2148px;width:187px;height:46px;line-height:46px">SIGH UP HERE</div>
</section>

<section>
  <div class="abs posts"></div>
  <h2 class="abs posts-title serif">Recent Posts</h2>
  <div class="abs thumb" style="left:78px;background:linear-gradient(135deg,#1b2a4a,#4a3a6a 60%,#20203a)" role="img" aria-label="Video thumbnail about product discovery tools"><span class="thumb-title">Trend Rocket Product Dis...</span></div>
  <div class="abs thumb" style="left:440px;background:linear-gradient(135deg,#111,#2a2a2a 55%,#1a3a70)" role="img" aria-label="Video thumbnail about starting with $500"><span class="thumb-title">Trend Rocket Product Dis...</span></div>
  <div class="abs thumb" style="left:800px;background:linear-gradient(135deg,#c9a070,#5a5a60 55%,#1a1a1a)" role="img" aria-label="Video thumbnail with a warning about products"><span class="thumb-title">Trend Rocket Product Dis...</span></div>
</section>

<footer>
  <div class="abs footer"></div>
  <p class="abs footer-nav">Home | Blog | My History | Top 100 Books | Contact</p>
  <p class="abs footer-copy">2018 ©DANE WHITAKER- All Rights Reserved.</p>
</footer>

</body>
</html>
```